Logo and label design for a poultry business

I would like a logo and Label design for our poultry business. Application will be similar to this. https://www.marvelstudio-example.com/harlow
We would like the designs in colours similar to ours. That is shades of red, yellow and turquoise. I've attached our current logo and pitch deck to see the design and colours that we've been using.
We would like to see how we can use both the text logo and the text logo with an icon. Ideally the icon will be a mascot that we can use on its own in different applications.
Sunny Roost is a unique small scale production franchise model that builds a value chain for poultry producers in Africa. A key component of Sunny Roost is modular retail, where we will brand freezers and freezer containers where the chicken will be sold directly to communities.
Target Market(s)
The design must be appealing to women without being too feminine. It must also be attractive in large retail shelves.
Industry/Entity Type
Agriculture, poultry, rural development
Look and feel
Each slider illustrates characteristics of the customer's brand and the style your logo design should communicate.

```html
<!DOCTYPE html>
<html lang="en">
<head>
<meta charset="utf-8">
<title>Sunny Roost – Chicken Breast Label</title>
<link rel="stylesheet" href="https://fonts.googleapis.com/css2?family=Baloo+2:wght@800&family=Hind:wght@600;700&family=Courgette&family=Barlow+Condensed:wght@400&display=swap">
<style>
  :root {
    --page: #ffffff;
    --cream: #fdf1c8;
    --cream-light: #fffdf3;
    --brand-blue: #02659a;
    --sky-blue: #0a9be0;
    --sand: #fbb870;
    --yellow: #ffe000;
    --white: #ffffff;
    --ink: #111111;
    --seal-red: #d51c26;
  }
  * { margin: 0; padding: 0; box-sizing: border-box; }
  html, body {
    width: 744px; height: 1200px; overflow: hidden;
    background: var(--page);
  }
  .canvas { position: relative; width: 744px; height: 1200px; }

  .label {
    position: absolute; left: 170px; top: 190px;
    width: 430px; height: 824px;
    background: var(--cream);
    overflow: hidden;
  }
  .label__sky {
    position: absolute; left: 0; top: 0; width: 430px; height: 440px;
    background: radial-gradient(circle at 50% 62%, var(--cream-light) 0%, var(--cream) 70%);
  }
  .brand {
    position: absolute; left: 0; top: 110px; width: 430px;
    display: flex; align-items: center; justify-content: center; gap: 12px;
  }
  .brand__dot {
    width: 26px; height: 26px; border-radius: 50%;
    background: var(--brand-blue);
  }
  .brand__name {
    font-family: "Baloo 2", sans-serif; font-weight: 800;
    font-size: 54px; line-height: 1; color: var(--brand-blue);
  }
  .farm-scene {
    position: absolute; left: 0; top: 232px; width: 430px; height: 150px;
    background: linear-gradient(180deg, var(--sand) 0%, var(--sky-blue) 45%, var(--brand-blue) 100%);
  }
  .panel {
    position: absolute; left: 0; top: 380px; width: 430px; height: 328px;
    background: var(--brand-blue);
  }
  .product-name {
    position: absolute; left: 0; top: 405px; width: 430px; text-align: center;
    font-family: "Hind", sans-serif; font-weight: 700;
    font-size: 64px; line-height: 64px; color: var(--white); letter-spacing: 0.5px;
  }
  .tagline {
    position: absolute; left: 0; top: 535px; width: 430px; text-align: center;
    font-family: "Courgette", cursive; font-size: 34px; line-height: 1;
    color: var(--yellow); letter-spacing: 1px;
  }
  .features {
    position: absolute; left: 20px; top: 590px; width: 396px;
    display: flex; justify-content: space-between;
    font-family: "Hind", sans-serif; font-weight: 600;
    font-size: 16.5px; line-height: 18px; color: var(--white); text-align: center;
  }
  .features__item { flex: 1; padding: 2px 0; }
  .features__item + .features__item { border-left: 2px dotted var(--yellow); }
  .net-weight {
    position: absolute; left: 29px; top: 660px;
    font-family: "Barlow Condensed", sans-serif; font-weight: 400;
    font-size: 36px; line-height: 1; color: var(--white);
  }
  .seal {
    position: absolute; left: 284px; top: 634px; width: 126px; height: 126px;
  }
  .notes {
    position: absolute; left: 29px; top: 724px;
    font-family: "Barlow Condensed", sans-serif; font-weight: 400;
    font-size: 16px; line-height: 21px; color: var(--ink);
  }
</style>
</head>
<body>
<div class="canvas">
  <section class="label">
    <div class="label__sky"></div>

    <div class="brand">
      <span class="brand__dot"></span>
      <span class="brand__name">Sunny Roost</span>
    </div>

    <div class="farm-scene" role="img" aria-label="Farm illustration with barn, silo, windmill, fence and chickens under sun-lit hills"></div>

    <div class="panel"></div>

    <h1 class="product-name">CHICKEN<br>BREAST</h1>
    <p class="tagline">Organic &amp; free range</p>

    <ul class="features" style="list-style:none">
      <li class="features__item">No added<br>hormones</li>
      <li class="features__item">100% Vegetarian<br>Feed</li>
      <li class="features__item">Always fresh &amp;<br>natural</li>
    </ul>

    <p class="net-weight">Net wt. 16 oz / 454g</p>

    <svg class="seal" viewBox="0 0 126 126" aria-hidden="true">
      <circle cx="63" cy="63" r="63" fill="var(--cream)"/>
      <circle cx="63" cy="63" r="56" fill="var(--seal-red)"/>
      <circle cx="63" cy="63" r="38" fill="var(--white)"/>
    </svg>

    <p class="notes">
      Keep refrigerated.<br>
      May contain up to two percent retained water<br>
      *Minimally processed, No artificial ingredients<br>
      *Federal regulations prohibit the use of hormones in chicken.
    </p>
  </section>
</div>
</body>
</html>
```